New Web Design Project shop crate

We are about to start a new furniture selling website and it will be based on shop crate . we mainly need two pages designing landing page & item page. so come up with your unique ideas and designs . Please make sure the design needs to be unique . no templates and themes . Will make the selected designer even happier if your design is selected. So basically over all it is going to be the new theme for our shop crate base eCommerce website .we will appreciate if its responsive with some unique features .
SO as per request of designers about more brief about the project = WE ONLY NEED A RESPONSIVE THEME FOR OUR SHOP CRATE BASE eCommerce WebSite . Mainly item page & product page needs a good unique design. Lighter, speed load, compatible with all browsers and responsive will be appreciated . To Get an idea check on sofahaven .co .uk website or chairmeadow etc.
more projects coming soon .

Target Market(s)

Our audience will be furniture buying customers .

Industry/Entity Type

Furniture

Requirements
Must have
• to get some sort of idea have a look at sofahaven .co uk`s website`s listing page and landing page .
Nice to have
• responsive, easy to customize, full theme .

```html
<!DOCTYPE html>
<html lang="en">
<head>
<meta charset="utf-8">
<title>Oak Nest – Furniture Store</title>
<link href="https://fonts.googleapis.com/css2?family=Open+Sans:wght@400;600;700&display=swap" rel="stylesheet">
<style>
:root{
  --teal:#1fb8c8;
  --orange:#f7941d;
  --ink:#333;
  --muted:#666;
  --line:#ddd;
  --bg:#e9e9e9;
  --panel:#f2f2f2;
  --white:#fff;
}
*{box-sizing:border-box;margin:0;padding:0}
html,body{width:857px;height:1200px;overflow:hidden}
body{background:var(--bg);font-family:'Open Sans',Arial,sans-serif;color:var(--ink);position:relative}
.page{position:absolute;left:114px;top:0;width:627px;height:1200px;background:var(--white);box-shadow:0 0 3px rgba(0,0,0,.15)}
.abs{position:absolute}
.inner{left:12px;width:603px}
.topbar{left:0;top:0;width:627px;height:21px;background:#dcdcdc;font-size:7px;display:flex;justify-content:flex-end;align-items:center;gap:13px;padding-right:12px;color:#222}
.logo{left:12px;top:35px;display:flex;align-items:center;gap:6px}
.logo-mark{width:38px;height:38px;background:var(--teal);border-radius:6px}
.logo-name{font-size:20px;font-weight:600;color:#222;line-height:1}
.contact{top:56px;font-size:7px;color:#555;display:flex;gap:6px;align-items:center}
.contact strong{display:block;font-size:10px;color:#111;font-weight:700}
.search{left:430px;top:57px;width:185px;height:23px;border:1px solid var(--line);display:flex}
.search span{flex:1;font-size:7px;color:#999;padding:7px 9px}
.search b{background:#f2f2f2;border-left:1px solid var(--line);font-size:8.5px;padding:6px 8px}
.cart{left:508px;top:33px;font-size:7px;display:flex;align-items:center;gap:4px}
.cart a{color:var(--orange);margin-left:3px}
.nav{top:98px;height:23px;background:var(--teal);display:flex;align-items:center;padding-left:2px}
.nav span{color:#fff;font-size:8.5px;font-weight:700;padding:0 7px;border-right:1px solid rgba(255,255,255,.3);line-height:23px}
.nav span:last-child{border:none}
.hero{top:121px;height:212px;background:linear-gradient(90deg,#d9d6cf 0%,#bfb9ad 30%,#e8e4dc 55%,#c86a2b 80%,#e7e1d8 100%)}
.promo{left:22px;top:44px;width:131px;height:112px;background:rgba(255,255,255,.85);padding:18px 14px}
.promo .big{font-size:30px;font-weight:600;color:#333;line-height:1}
.promo .big em{font-style:normal;font-size:11px;color:var(--teal);font-weight:600}
.promo p{font-size:7.8px;color:#555;line-height:1.55;margin-top:8px}
.dots{display:flex;gap:3px}
.dot{width:7px;height:7px;border-radius:50%;background:#fff}
.dot.on{background:#ffc20e}
.features{top:341px;height:54px;display:flex;gap:7px}
.feature{flex:1;border:1px solid var(--line);display:flex;align-items:center;justify-content:space-between;padding:0 8px}
.feature .ico{width:34px;height:34px;border-radius:50%;background:#eee;border:1px solid #ddd;display:flex;align-items:center;justify-content:center}
.feature .txt{text-align:right}
.feature b{display:block;font-size:12px;font-weight:600;color:#111}
.feature small{font-size:7.5px;color:#666}
.heading{left:0;width:627px;text-align:center;font-size:13px;font-weight:700;color:#222}
.products{top:435px;height:196px;display:flex;gap:11px}
.card{flex:1;border:1px solid var(--line);padding:14px 11px 0}
.photo{height:80px;margin:0 auto 16px;width:60px;border-radius:3px}
.card h3{font-size:7.5px;font-weight:400;line-height:1.65;color:#333}
.price{font-size:7.5px;font-weight:700;margin-top:8px}
.price span{color:var(--orange)}
.btn{display:inline-block;background:var(--orange);color:#fff;font-size:7.5px;padding:3px 8px;margin-top:5px}
.arrows{left:296px;top:642px;display:flex;gap:4px}
.arrow{width:16px;height:16px;border-radius:50%;background:#888;display:flex;align-items:center;justify-content:center}
.divider{left:60px;width:507px;height:1px;background:linear-gradient(90deg,transparent,#ddd,transparent)}
.testis{top:724px;display:flex;gap:20px}
.testi{flex:1;display:flex;gap:12px}
.avatar{width:61px;height:61px;border-radius:50%;background:radial-gradient(circle at 50% 40%,#c9a78e,#4a5560);flex:none}
.testi p{font-size:7.5px;line-height:1.65;color:#333}
.testi b{display:block;font-size:7.5px;margin-top:6px}
.testi small{font-size:7.5px;color:#666}
.tdots{left:299px;top:809px;display:flex;gap:5px}
.tdot{width:7px;height:7px;border-radius:50%;background:#bbb}
.tdot.on{background:var(--orange)}
.brands{top:897px;height:34px;display:flex;align-items:center;justify-content:space-between}
.brand{font-size:13px;color:#999;font-weight:400}
.sep{width:1px;height:18px;background:#ccc}
.footer{left:0;top:958px;width:627px;height:172px;background:var(--panel)}
.col{position:absolute;top:14px;font-size:7px;line-height:14px;color:#444}
.col h4{font-size:8px;font-weight:700;color:#222;margin-bottom:4px}
.col .sub{font-weight:700;color:#222}
.social{display:flex;align-items:center;gap:7px;height:28px}
.social i{width:20px;height:20px;border-radius:50%;display:block}
.signup{position:absolute;left:450px;top:131px;width:163px;height:23px;display:flex;border:1px solid var(--line);background:#fff}
.signup span{flex:1;font-size:7px;color:#999;padding:7px 9px}
.signup b{background:var(--orange);color:#fff;font-size:7.5px;padding:6px 6px}
.bottom{left:0;top:1130px;width:627px;height:70px;background:#e4e4e4;text-align:center}
.bottom p{font-size:6px;color:#333;margin-top:15px}
.cards{display:flex;justify-content:center;gap:6px;margin-top:12px}
.cards i{width:30px;height:18px;display:block;background:#dfe6ef;border:1px solid #c6cdd6;border-radius:2px}
</style>
</head>
<body>
<div class="page">
  <div class="abs topbar"><span>Login</span><span>Signup</span><span>My Account</span><span>Order Status</span><span>Wish List</span></div>

  <div class="abs logo"><div class="logo-mark"></div><div class="logo-name">Oak Nest</div></div>

  <div class="abs contact" style="left:179px">
    <svg width="14" height="16" viewBox="0 0 14 16"><path d="M3 1l3 3-2 2c1 2 3 4 5 5l2-2 3 3-2 3C6 15 0 9 1 3z" fill="#f7941d"/></svg>
    <div>talk to a real person<strong>(555) 014 228</strong></div>
  </div>
  <div class="abs contact" style="left:298px">
    <svg width="20" height="18" viewBox="0 0 20 18"><rect x="1" y="5" width="15" height="10" rx="1" fill="none" stroke="#f7941d" stroke-width="2"/><circle cx="15" cy="5" r="4.5" fill="#f7941d"/></svg>
    <div>chat with a real person<strong>LIVE CHAT NOW</strong></div>
  </div>

  <div class="abs cart">
    <svg width="14" height="12" viewBox="0 0 14 12"><path d="M0 1h3l2 7h7l2-5H4" fill="none" stroke="#1fb8c8" stroke-width="1.6"/><circle cx="6" cy="10.5" r="1.2" fill="#1fb8c8"/><circle cx="11" cy="10.5" r="1.2" fill="#1fb8c8"/></svg>
    <span>0Items <b>($0.00)</b><a>Checkout</a></span>
  </div>

  <div class="abs search"><span>Search Keyword</span><b>SEARCH</b></div>

  <div class="abs inner nav"><span>HOME</span><span>BEDROOM</span><span>LIVING ROOM</span><span>DINING ROOM</span><span>OFFICE</span><span>BRANDS</span><span>SALE</span></div>

  <div class="abs inner hero" role="img" aria-label="Photo of a bright bedroom with an orange bed, shelving and a garden view">
    <div class="abs promo">
      <div class="big">60% <em>OFF</em></div>
      <p>Lorem Ipsum is simply dummy text of the printing and typesetting industry.</p>
    </div>
    <div class="abs dots" style="left:270px;top:193px"><i class="dot on"></i><i class="dot"></i><i class="dot"></i></div>
  </div>

  <div class="abs inner features">
    <div class="feature"><div class="ico"><svg width="12" height="14" viewBox="0 0 12 14"><path d="M3 6V4a3 3 0 016 0v2" fill="none" stroke="#666" stroke-width="1.5"/><rect x="1" y="6" width="10" height="8" rx="1" fill="#666"/></svg></div><div class="txt"><b>100 %</b><small>Secure Shopping</small></div></div>
    <div class="feature"><div class="ico"><svg width="16" height="12" viewBox="0 0 16 12"><path d="M1 1h9v8H1zM10 4h3l2 3v2h-5" fill="none" stroke="#666" stroke-width="1.2"/><circle cx="4" cy="10" r="1.5" fill="#666"/><circle cx="12" cy="10" r="1.5" fill="#666"/></svg></div><div class="txt"><b>Shipping</b><small>Free</small></div></div>
    <div class="feature"><div class="ico"><svg width="16" height="16" viewBox="0 0 16 16"><path d="M2 9V7a6 6 0 0112 0v2" fill="none" stroke="#666" stroke-width="1.3"/><rect x="1" y="8" width="3" height="5" rx="1" fill="#666"/><rect x="12" y="8" width="3" height="5" rx="1" fill="#666"/></svg></div><div class="txt"><b>Support</b><small>Customer Service</small></div></div>
    <div class="feature"><div class="ico"><svg width="14" height="16" viewBox="0 0 14 16"><circle cx="7" cy="6" r="5" fill="none" stroke="#666" stroke-width="1.5"/><circle cx="7" cy="6" r="2" fill="#666"/><path d="M4 10l-1 5 2-1 1 1 1-4M10 10l1 5-2-1-1 1-1-4" fill="#666"/></svg></div><div class="txt"><b>Money</b><small>Back Guarantee</small></div></div>
  </div>

  <div class="abs heading" style="top:408px">Best Sellers</div>

  <div class="abs inner products">
    <div class="card"><div class="photo" role="img" aria-label="Oak dining chair with brown leather seat" style="background:linear-gradient(#c98a3c,#8a5520)"></div><h3>Kestrel Petite Oak Dining Chair with Chocolate Leather Seat</h3><div class="price">Our Price: <span>£135.70</span></div><span class="btn">More Info</span></div>
    <div class="card"><div class="photo" role="img" aria-label="Pine double wardrobe" style="background:linear-gradient(#c9a062,#9a7438)"></div><h3>Kestrel Petite Oak Dining Chair with Chocolate Leather Seat</h3><div class="price">Our Price: <span>£135.70</span></div><span class="btn">More Info</span></div>
    <div class="card"><div class="photo" role="img" aria-label="Red dining chair" style="background:linear-gradient(#d3282c,#8e1518);width:40px"></div><h3>Kestrel Petite Oak Dining Chair with Chocolate Leather Seat</h3><div class="price">Our Price: <span>£135.70</span></div><span class="btn">More Info</span></div>
    <div class="card"><div class="photo" role="img" aria-label="Wooden sideboard with wine rack" style="background:linear-gradient(#b57b3e,#7f4f22);width:70px;height:50px;margin-top:15px;margin-bottom:31px"></div><h3>Kestrel Petite Oak Dining Chair with Chocolate Leather Seat</h3><div class="price">Our Price: <span>£135.70</span></div><span class="btn">More Info</span></div>
    <div class="card"><div class="photo" role="img" aria-label="Dark pine wardrobe" style="background:linear-gradient(#a87640,#6e4620);width:44px"></div><h3>Kestrel Petite Oak Dining Chair with Chocolate Leather Seat</h3><div class="price">Our Price: <span>£135.70</span></div><span class="btn">More Info</span></div>
  </div>

  <div class="abs arrows">
    <div class="arrow"><svg width="6" height="6" viewBox="0 0 6 6"><path d="M5 0v6L0 3z" fill="#fff"/></svg></div>
    <div class="arrow"><svg width="6" height="6" viewBox="0 0 6 6"><path d="M1 0v6l5-3z" fill="#fff"/></svg></div>
  </div>

  <div class="abs divider" style="top:674px"></div>
  <div class="abs heading" style="top:687px">Customer Testimonials</div>

  <div class="abs inner testis">
    <div class="testi"><div class="avatar" role="img" aria-label="Customer portrait"></div><div><p>Lorem Ipsum is simply dummy text of the printing and typesetting industry. Lorem Ipsum has been the industry's standard dummy text ever since the 1500s, when an known printer took a galley</p><b>Tom Reyes</b><small>CEO, Founder</small></div></div>
    <div class="testi"><div class="avatar" role="img" aria-label="Customer portrait"></div><div><p>Lorem Ipsum is simply dummy text of the printing and typesetting industry. Lorem Ipsum has been the industry's standard dummy text ever since the 1500s, when an known printer took a galley</p><b>Tom Reyes</b><small>CEO, Founder</small></div></div>
  </div>
  <div class="abs tdots"><i class="tdot on"></i><i class="tdot"></i><i class="tdot"></i></div>

  <div class="abs divider" style="top:841px"></div>
  <div class="abs heading" style="top:858px">Brands</div>

  <div class="abs inner brands">
    <span class="brand">Larchwood</span><i class="sep"></i>
    <span class="brand">Hollow Elm</span><i class="sep"></i>
    <span class="brand">Keel Works</span><i class="sep"></i>
    <span class="brand">Bramble Co</span><i class="sep"></i>
    <span class="brand">Norvale</span><i class="sep"></i>
    <span class="brand">Larchwood</span>
  </div>

  <footer class="abs footer">
    <div class="col" style="left:12px"><h4>What We Sell</h4><div class="sub">Bedroom</div>Beds<br>Dressing Tables<br>Bedside Tables<br>Stools<br>Chest Of Drawers<br>Mattresses<br>Lamp Tables<br>Wardrobes</div>
    <div class="col" style="left:128px;top:32px"><div class="sub">Living Room</div>Bookcases<br>Media TV/ Units<br>Display<br>Coffe Table<br>Sofas<br>Dressers<br>Footstools</div>
    <div class="col" style="left:239px;top:32px"><div class="sub">Dining Room</div>Bookcases<br>Media TV/ Units<br>Display<br>Coffe Table<br>Sofas<br>Dressers<br>Footstools</div>
    <div class="col" style="left:339px;top:32px"><div class="sub">About Us</div>Security and Privacy<br>Secure Payments<br>Our Location<br>Site Map<br>FAQs<br>Buying Guide<br>Furniture Care</div>
    <div class="col" style="left:448px"><h4>Additional Info</h4>Customer Service<br>Shipping &amp; Delivery<br>Return Policy<br>Reseller Program<br>Privacy Policy<h4 style="margin-top:10px">Sign Up for Special Deals</h4></div>
    <div class="col" style="left:549px"><h4>Follow Us</h4>
      <div class="social"><i style="background:#3b5998"></i>Friendpage</div>
      <div class="social"><i style="background:#3ea6dd"></i>Chirper</div>
      <div class="social"><i style="background:#d9251c"></i>ViewTube</div>
    </div>
    <div class="signup"><span>Your Email Address</span><b>Sign Up</b></div>
  </footer>

  <div class="abs bottom">
    <p>Copyright 2014 company name. All Rights Reserved</p>
    <div class="cards"><i></i><i></i><i></i><i></i><i></i><i></i></div>
  </div>
</div>
</body>
</html>
```